PEACFUL ACUPUNCTURE PRACTITIONER NEEDS A NEW COAT

I need a new design for an exiting website http://willowgateneedlework.com/ for a acupuncturist. This will be a minimalism design with lots and lots of white space. Home page and one interior page. Please keep the feeling of calm and peaceful serenity. For Color scheme: https://www.morningfernclinic.com/fertility. The bottom part of the home page with sections and links to the service pages: https://harborlotuswellness.com/. The client likes this the best: http://mfclinic.com/. I'm attaching the logo and content pages.

Target Market(s)

Women

Industry/Entity Type

Wellness, health, wellbeing, meditation

Number of Pages Required

2 page

Font styles to use
Sans Serif
Decorative

Colors

Designer to choose colors to be used in the design.

Requirements
Must have
Nice to have
• Follow new website drafts and links
Should not have
• Busy with bright colors. No poping

```html
<!DOCTYPE html>
<html lang="en">
<head>
<meta charset="utf-8">
<title>Willowgate Needlework — Home</title>
<link href="https://fonts.googleapis.com/css2?family=Mulish:ital,wght@0,300;0,400;0,600;0,700;1,400&display=swap" rel="stylesheet">
<style>
:root{
  --canvas:#ffffff;
  --page:#f8f8f8;
  --ink:#5a5a5a;
  --ink-soft:#8a8a8a;
  --rose:#b88a8e;
  --rose-line:#c49ca0;
  --blush:#f5e5e5;
  --bar:#787878;
  --footer:#3e3c3c;
  --footer-text:#d9d9d9;
  --white:#ffffff;
  --slate-dark:#353946;
  --slate:#4b4f5c;
  --slate-light:#5e616a;
}
*{margin:0;padding:0;box-sizing:border-box}
html,body{width:1200px;height:1200px;overflow:hidden;background:var(--canvas)}
body{font-family:'Mulish',sans-serif;color:var(--ink)}
.stage{position:absolute;left:0;top:0;width:1932px;height:1932px;transform:scale(.6211);transform-origin:0 0}
.page{position:absolute;left:701px;top:0;width:461px;height:1932px;background:var(--page);overflow:hidden}
.abs{position:absolute}
.notice{left:0;top:0;width:461px;height:10px;background:var(--bar);color:var(--white);font-size:4px;text-align:center;line-height:10px;white-space:nowrap}
.notice b{font-weight:700}.notice span{color:#e6c4c7}
.brand{left:0;top:27px;width:461px;display:flex;justify-content:center;align-items:center;gap:6px}
.brand-mark{width:16px;height:16px;border-radius:50%;background:var(--rose);opacity:.75}
.brand-name{font-size:11px;color:var(--ink);line-height:1;letter-spacing:.3px}
.nav{left:0;top:64px;width:461px;display:flex;justify-content:center;gap:20px;font-size:4.3px;color:var(--ink-soft)}
.nav .active{color:var(--rose);border-bottom:1px solid var(--rose);padding-bottom:4px}
.hero{left:0;top:86px;width:461px;height:265px;background:linear-gradient(100deg,var(--slate-dark) 0,var(--slate) 50%,var(--slate-light) 100%)}
.hero-title{left:46px;top:131px;font-size:21.5px;font-weight:600;color:var(--white);line-height:23px}
.hero-sub{left:46px;top:187px;font-size:8.4px;color:var(--white);line-height:11px}
.btn{background:var(--rose);color:var(--white);font-size:4.3px;text-align:center;letter-spacing:.3px;text-transform:uppercase;white-space:nowrap}
.section-title{font-size:15px;font-weight:600;color:var(--ink)}
.h-mid{font-size:11.5px;font-weight:600;color:var(--ink)}
.body-copy{font-size:4.4px;line-height:9px;color:var(--ink-soft)}
.blush{background:var(--blush)}
.rule{height:1px;background:var(--rose-line)}
.focus{width:84px}
.focus .kicker{font-size:3.6px;letter-spacing:1.3px;color:var(--ink-soft);margin-top:10px}
.focus .name{font-size:7px;font-weight:600;font-style:italic;color:var(--ink);margin:4px 0 5px}
.photo{display:block}
.footer{left:0;top:1736px;width:461px;height:196px;background:var(--footer);color:var(--footer-text)}
.f-head{font-size:6.2px;letter-spacing:.3px}
.hours{width:86px;font-size:4.4px}
.hours div{display:flex;justify-content:space-between;border-top:1px solid #5a5858;height:18.2px;align-items:center}
.hours span:last-child{color:var(--rose)}
.insta{display:grid;grid-template-columns:repeat(4,21px);gap:3px}
.insta i{display:block;width:21px;height:21px;background:linear-gradient(135deg,#8a7a78,#c9a79f)}
.insta i:nth-child(3n){background:linear-gradient(135deg,#5b5456,#a39390)}
.insta i:nth-child(4n+1){background:linear-gradient(135deg,#b69a85,#e0cfc2)}
.email{width:117px;height:20px;background:var(--white);font-size:4.3px;color:#aaa;padding:0 7px;display:flex;align-items:center;justify-content:space-between}
</style>
</head>
<body>
<div class="stage">
<div class="page">

  <div class="abs notice"><b>Pandemic Update:</b> We are open and welcoming new patients, with care steps in place to keep our clients and our town safe. <span>Read More</span></div>

  <div class="abs brand"><span class="brand-mark"></span><span class="brand-name">Willowgate Needlework</span></div>
  <nav class="abs nav">
    <span class="active">Home</span><span>About</span><span>Fertility &amp; Pregnancy</span><span>Emotional Well Being</span><span>Hormone Balance</span><span>Strength &amp; Structure</span>
  </nav>

  <div class="abs hero photo" role="img" aria-label="Dark slate wooden table with acupuncture needles in a stone bowl, black stones, green leaves and a bowl of dried herbs"></div>
  <h1 class="abs hero-title">Acupuncture &amp;<br>Natural Medicine</h1>
  <p class="abs hero-sub">Specializing In Women's Health, Fertility<br>Challenges &amp; Pregnancy Care</p>
  <div class="abs btn" style="left:46px;top:223px;width:85px;height:15px;line-height:15px">Book An Appointment</div>

  <h2 class="abs section-title" style="left:0;width:480px;text-align:center;top:375px">Philosophy Of Care</h2>
  <div class="abs body-copy" style="left:204px;top:418px;width:176px">
    <p>Acupuncture &amp; Chinese Herbal Medicine are rooted in over 3000 years of history and tradition. As a complete medical system that has remained flexible and relevant we honor what has worked from the past while embracing the medicine of tomorrow.</p>
    <p style="margin-top:9px">At Willowgate Needlework we provide compassionate, respectful and empowering care in a safe and inclusive environment. Our goal is to harmonize physical, mental and emotional wellbeing to strengthen the calm point from which we all strive to live.</p>
  </div>

  <div class="abs blush" style="left:46px;top:559px;width:53px;height:54px"></div>
  <div class="abs rule" style="left:46px;top:559px;width:360px"></div>
  <svg class="abs" style="left:396px;top:549px" width="20" height="20" aria-hidden="true"><circle cx="10" cy="10" r="9" fill="var(--blush)"/><circle cx="10" cy="10" r="3" fill="var(--rose)" opacity=".7"/></svg>
  <h2 class="abs h-mid" style="left:78px;top:571px">Areas Of Focus</h2>

  <div class="abs focus" style="left:46px;top:638px">
    <svg width="24" height="24" viewBox="0 0 24 24" fill="none" stroke="var(--rose)" stroke-width=".9"><circle cx="12" cy="12" r="11"/><path d="M12 1a5.5 5.5 0 0 1 0 11a5.5 5.5 0 0 0 0 11"/><circle cx="12" cy="6.5" r="1.3" fill="var(--rose)"/><circle cx="12" cy="17.5" r="1.3"/></svg>
    <div class="kicker">NEST</div><div class="name">Fertility &amp; Pregnancy</div>
    <p class="body-copy">Our goal is to help build families and we happily embrace the diversity that word includes. We warmly welcome the LGBTQ community, single mothers and parents by choice and surrogates.</p>
  </div>
  <div class="abs focus" style="left:141px;top:638px">
    <svg width="24" height="24" viewBox="0 0 24 24" fill="none" stroke="var(--rose)" stroke-width=".9"><ellipse cx="12" cy="19" rx="10" ry="4" fill="var(--rose)" opacity=".5"/><ellipse cx="12" cy="12.5" rx="8" ry="3.5"/><ellipse cx="12" cy="6" rx="5" ry="3"/></svg>
    <div class="kicker">ROCKS</div><div class="name">Hormone Balance</div>
    <p class="body-copy">Our hormones are constantly shifting and occasionally this internal orchestra needs to be refined. Acupuncture works to help the body rediscover the positive patterns.</p>
  </div>
  <div class="abs focus" style="left:236px;top:638px">
    <svg width="24" height="24" viewBox="0 0 24 24" fill="none" stroke="var(--rose)" stroke-width=".9"><path d="M4 22C4 10 10 3 21 2C21 13 14 20 4 22Z" fill="var(--rose)" opacity=".55"/><path d="M4 22L16 8"/></svg>
    <div class="kicker">TREE</div><div class="name">Strength &amp; Structure</div>
    <p class="body-copy">Our bodies carry us through all we do. Sometimes they need attention and support. Whether you need a simple "tune up" or help recovering from surgery or illness acupuncture can help.</p>
  </div>
  <div class="abs focus" style="left:331px;top:638px">
    <svg width="28" height="24" viewBox="0 0 28 24" fill="none" stroke="var(--rose)" stroke-width=".9"><path d="M14 3C10 8 10 14 14 19C18 14 18 8 14 3Z"/><path d="M14 19C10 17 6 13 5 8C9 9 12 13 14 19Z"/><path d="M14 19C18 17 22 13 23 8C19 9 16 13 14 19Z"/><path d="M4 19Q14 24 24 19"/></svg>
    <div class="kicker">HEART</div><div class="name">Emotional Well Being</div>
    <p class="body-copy">Our mental and emotional wellness is imperative to whole body healing. Acupuncture and herbs can help reset patterns of relaxation while teaching the body to access these resources more easily on its own.</p>
  </div>

  <div class="abs blush" style="left:141px;top:837px;width:184px;height:236px"></div>
  <div class="abs photo" style="left:109px;top:797px;width:108px;height:108px;background:linear-gradient(135deg,#b9b4b0,#8a6b4f 55%,#dcd8d2)" role="img" aria-label="Amber bottle with herbal capsules, glass jar and a mortar with fresh herbs"></div>
  <h2 class="abs h-mid" style="left:266px;top:851px">Shop Our Products</h2>
  <p class="abs body-copy" style="left:78px;top:934px;width:108px">Shop herbs and supplements for treating everything from the common cold and flu to even the most stubborn and chronic issues.</p>
  <div class="abs btn" style="left:78px;top:974px;width:53px;height:15px;line-height:15px">Shop Now</div>
  <div class="abs photo" style="left:204px;top:934px;width:180px;height:175px;background:radial-gradient(circle at 35% 55%,#7a4e3a 0,#a07554 40%,#c8ab85 70%,#e8ddd0 100%)" role="img" aria-label="Wooden tray of dried Chinese herbs beside a paper scroll with brush script"></div>

  <div class="abs blush" style="left:0;top:1161px;width:461px;height:222px"></div>
  <div class="abs photo" style="left:46px;top:1190px;width:150px;height:238px;background:linear-gradient(160deg,#cdb6a6 0,#e9ddd5 40%,#f4f1ef 100%)" role="img" aria-label="Woman relaxing with eyes closed during a gentle head treatment"></div>
  <h2 class="abs h-mid" style="left:166px;top:1209px">Natural Healing</h2>
  <p class="abs" style="left:166px;top:1232px;font-size:6.3px;line-height:8.5px;color:var(--ink-soft)">Specializing In Women's Health, Fertility<br>Challenges &amp; Pregnancy Care</p>
  <div class="abs btn" style="left:210px;top:1265px;width:86px;height:15px;line-height:15px">Book An Appointment</div>

  <div class="abs blush" style="left:46px;top:1490px;width:59px;height:53px"></div>
  <div class="abs rule" style="left:46px;top:1490px;width:360px"></div>
  <svg class="abs" style="left:396px;top:1480px" width="20" height="20" aria-hidden="true"><circle cx="10" cy="10" r="9" fill="var(--blush)"/><circle cx="10" cy="10" r="3" fill="var(--rose)" opacity=".7"/></svg>
  <h2 class="abs h-mid" style="left:78px;top:1501px">Testimonials</h2>
  <div class="abs photo" style="left:211px;top:1543px;width:24px;height:24px;border-radius:50%;background:linear-gradient(135deg,#a98072,#e6d2c8);box-shadow:0 0 0 2px #fff" role="img" aria-label="Client portrait"></div>
  <p class="abs" style="left:0;width:446px;text-align:center;top:1576px;font-size:6px;font-weight:600;color:var(--ink)">Maren T.</p>
  <p class="abs" style="left:0;width:446px;text-align:center;top:1590px;font-size:7px;letter-spacing:1px;color:var(--rose)">★★★★★</p>
  <p class="abs body-copy" style="left:101px;top:1624px;width:264px;text-align:center;font-style:italic">I went to Willowgate Needlework as my very first experience with acupuncture, so I was quite nervous imagining those little needles hurting as they go in, but Lena was very kind and professional and clearly explained everything and what I might feel when the pins go in and it was really amazing how you don't even feel that they are there and yet you feel this gentle stirring and healing going on internally. I would highly recommend this practice, and Lena has great knowledge of Chinese medicine and has been kind enough to even lend me one of her books since I am very curious to learn more myself. It's been a great experience and I appreciate that she has a sliding scale so it's something that is more affordable to do on a regular basis.</p>

  <footer class="abs footer">
    <div class="abs f-head" style="left:46px;top:26px">HOURS</div>
    <div class="abs hours" style="left:46px;top:48px">
      <div><span>Monday</span><span>Closed</span></div>
      <div><span>Tuesday</span><span>10 am - 6 pm</span></div>
      <div><span>Wednesday</span><span>10 am - 6 pm</span></div>
      <div><span>Thursday</span><span>10 am - 6 pm</span></div>
      <div><span>Friday</span><span>10 am - 6 pm</span></div>
      <div><span>Saturday</span><span>10 am - 3 pm</span></div>
      <div><span>Sunday</span><span>Closed</span></div>
    </div>
    <div class="abs f-head" style="left:172px;top:26px">INSTAGRAM FEED</div>
    <div class="abs insta" style="left:172px;top:50px" role="img" aria-label="Grid of recent photo posts">
      <i></i><i></i><i></i><i></i><i></i><i></i><i></i><i></i><i></i><i></i>
      <i></i><i></i><i></i><i></i><i></i><i></i><i></i><i></i><i></i><i></i>
    </div>
    <div class="abs f-head" style="left:299px;top:26px">NEWSLETTER</div>
    <p class="abs" style="left:299px;top:49px;font-size:4.6px">Subscribe to our newsletter</p>
    <div class="abs email" style="left:299px;top:72px"><span>Email</span>
      <svg width="7" height="7" viewBox="0 0 10 10" fill="none" stroke="#777" stroke-width="1"><path d="M1 9L2 6L7 1L9 3L4 8Z"/></svg></div>
    <div class="abs btn" style="left:299px;top:104px;width:53px;height:15px;line-height:15px">Subscribe Now</div>
    <p class="abs" style="left:299px;top:159px;font-size:3.4px;color:#bdbdbd">© 2022 Willowgate Needlework. All Rights Reserved.</p>
    <p class="abs" style="left:299px;top:166px;font-size:3.4px;color:var(--rose)">Privacy Policy | Terms Of Use</p>
  </footer>

</div>
</div>
</body>
</html>
```